Law Firm Needs Brochure Redesign Using New Logo

We are a personal injury law firm that does auto injuries and other personal injury cases. We want a new brochure that has our updated logo and information. Instead of gold and black, we want more navy, as matches the new logo. The Auto Liability portion should read: "(required by the state of Arizona in the amounts of $25,000 per person / $50,000 per accident, but a higher amount may be best )." The other information can remain the same. We'd like the brochure to keep the same professional tone as the previous brochure.
Our website is https://www.marbrenlegal.com/.

```html
<!DOCTYPE html>
<html lang="en">
<head>
<meta charset="utf-8">
<title>Marbren Legal – Car Accident Brochure</title>
<link href="https://fonts.googleapis.com/css2?family=Cinzel:wght@400;600;700&family=Open+Sans:ital,wght@0,400;0,600;1,400&display=swap" rel="stylesheet">
<style>
  :root{
    --navy:#15244a;
    --navy-deep:#0f1b38;
    --ink:#4a4f5c;
    --rule:#c9ccd4;
    --paper:#ffffff;
    --backdrop:#a9abaf;
    --car-1:#2b3a82;
    --car-2:#18214f;
    --photo-1:#d9d9db;
    --photo-2:#8e9096;
  }
  *{box-sizing:border-box;margin:0;padding:0}
  html,body{width:1130px;height:1200px;overflow:hidden}
  body{background:var(--backdrop);font-family:"Open Sans",Arial,sans-serif;color:var(--ink);position:relative}
  .spread{position:absolute;left:165px;width:800px;height:570px;background:var(--paper);box-shadow:0 4px 14px rgba(0,0,0,.25);display:flex;overflow:hidden}
  .spread--outside{top:20px}
  .spread--inside{top:610px}
  .serif{font-family:"Cinzel",Georgia,serif}

  /* outside */
  .panel{height:100%;position:relative}
  .panel--flap{width:266px;border-right:1px solid var(--rule);text-align:center;padding:36px 20px 0}
  .panel--back{width:266px;border-right:1px solid var(--rule)}
  .panel--cover{width:268px}
  .brand{display:flex;align-items:center;justify-content:center;gap:10px;color:var(--navy)}
  .brand__dot{width:30px;height:30px;border-radius:50%;background:var(--navy)}
  .brand__name{font-family:"Cinzel",Georgia,serif;font-weight:700;font-size:22px;letter-spacing:1px}
  .stat{margin-top:56px;color:var(--navy)}
  .stat + .stat{margin-top:44px}
  .stat__over{font-family:"Cinzel",Georgia,serif;font-size:16px}
  .stat__num{font-family:"Cinzel",Georgia,serif;font-weight:700;font-size:32px;line-height:1}
  .stat__note{font-size:10px;color:var(--ink);margin-top:6px;line-height:1.35}
  .flap__rule{width:160px;height:2px;background:var(--navy-deep);margin:58px auto 22px}
  .flap__text{font-size:10.5px;line-height:1.4;color:var(--ink)}
  .car{position:absolute;left:388px;top:160px;width:284px;height:410px;border-radius:120px 120px 10px 10px;background:linear-gradient(180deg,var(--car-1),var(--car-2) 55%,#24306a)}
  .car__fold{position:absolute;left:532px;top:160px;width:4px;height:410px;background:var(--paper)}
  .cover__title{position:absolute;right:18px;top:14px;text-align:right;color:var(--navy-deep);font-family:"Cinzel",Georgia,serif;font-weight:700;font-size:15px;line-height:1.3}
  .cover__sub{position:absolute;right:18px;top:66px;width:240px;text-align:center;font-style:italic;font-size:11px;line-height:1.35}
  .cover__sub span{display:inline-block;border-bottom:1px solid var(--navy-deep);padding:0 4px}
  .cover__address{position:absolute;right:0;bottom:18px;writing-mode:vertical-rl;font-size:12px;line-height:1.3;color:var(--navy-deep);width:36px;height:190px}

  /* inside */
  .panel--tips{width:268px;border-right:1px solid var(--rule);padding:14px 12px 0 28px}
  .tips__title{font-family:"Cinzel",Georgia,serif;font-size:13px;color:var(--navy);margin-bottom:8px;position:relative}
  .tips__title::before{content:"";position:absolute;left:-28px;top:8px;width:20px;height:2px;background:var(--navy)}
  .tip{font-size:8.6px;line-height:1.3;margin-bottom:7px;position:relative}
  .tip::before{content:"";position:absolute;left:-28px;top:3px;width:22px;height:2.5px;background:var(--navy)}
  .tip b{font-weight:600;color:var(--navy)}
  .inner{width:532px;height:100%;position:relative}
  .inner__photo{height:244px;background:linear-gradient(100deg,var(--photo-1),var(--photo-2) 45%,#c9cacc 70%,#5d6069)}
  .inner__bar{height:33px;background:var(--navy);display:flex;align-items:flex-end;padding:0 0 6px 26px;color:#fff;font-family:"Cinzel",Georgia,serif;font-size:12px}
  .inner__bar span:first-child{width:300px}
  .inner__body{display:flex;height:293px}
  .col-coverage{width:269px;padding:10px 14px 0 12px;font-size:8.8px;line-height:1.3}
  .col-coverage p{margin-bottom:8px}
  .col-coverage b,.col-behavior b{font-weight:600;color:var(--navy)}
  .strip{width:36px;background:var(--navy);display:flex;flex-direction:column;align-items:center;padding-top:26px}
  .strip svg{display:block}
  .strip__contact{margin-top:auto;margin-bottom:10px;display:flex;flex-direction:column;gap:8px;align-items:center}
  .col-behavior{width:227px;padding:10px 12px 0 12px;font-size:8.8px;line-height:1.3}
  .col-behavior h3{font-family:"Cinzel",Georgia,serif;font-weight:400;font-size:12px;color:var(--navy);margin:8px 0 4px}
  .contact{border-top:1px solid var(--navy);margin:8px -12px 0 -12px;padding:4px 12px 0}
  .contact h3{margin:0 0 6px}
  .contact p{margin-bottom:4px}
</style>
</head>
<body>

<section class="spread spread--outside" aria-label="Brochure outside">
  <div class="panel panel--flap">
    <div class="brand"><span class="brand__dot"></span><span class="brand__name">MARBREN LEGAL</span></div>
    <div class="stat">
      <div class="stat__over">OVER</div>
      <div class="stat__num">107,000</div>
      <div class="stat__note">crashes will happen in the state of<br>Arizona this year</div>
    </div>
    <div class="stat">
      <div class="stat__over">OVER</div>
      <div class="stat__num">700</div>
      <div class="stat__note">of them will result in fatalities.</div>
    </div>
    <div class="flap__rule"></div>
    <p class="flap__text">If we don't win, you don't pay attorney fees. That seems fair to us. Know what's happening with your case, get the answers to your questions and work on getting better with the confidence that you've got an excellent group of people working for you.</p>
  </div>
  <div class="panel panel--back"></div>
  <div class="panel panel--cover">
    <h1 class="cover__title">Protect your family in<br>case of a car accident</h1>
    <p class="cover__sub">A little knowledge and preparation<br><span>go a long way</span></p>
    <p class="cover__address">4870 N. 19th Avenue Suite<br>B310 Phoenix AZ 85015</p>
  </div>
  <div class="car" role="img" aria-label="Top-down view of a dark blue sports car"></div>
  <div class="car__fold"></div>
</section>

<section class="spread spread--inside" aria-label="Brochure inside">
  <div class="panel panel--tips">
    <h2 class="tips__title">Top 10 Tips to Avoid a Crash</h2>
    <p class="tip"><b>Anyone making a left turn must wait for all oncoming traffic to clear before proceeding.</b> Yes, even if the light has turned yellow. Wait to be sure that all traffic has stopped.</p>
    <p class="tip"><b>When your light turns green,</b> check to be sure that no vehicles are entering the intersection late.</p>
    <p class="tip"><b>Allow plenty of room between you and the car in front of you.</b> Traffic can stop in an instant, even if you can't see anything ahead.</p>
    <p class="tip"><b>Avoid being distracted.</b> Teenagers are especially susceptible to losing focus if there are too many friends in the car.</p>
    <p class="tip"><b>Keep the volume of your radio down and never wear headphones.</b> Cars are very soundproof these days, but you need to be able to hear an ambulance or police siren.</p>
    <p class="tip"><b>Be especially careful on the weekends and early morning hours.</b></p>
    <p class="tip"><b>Don't speed.</b> Speed is a factor in most crashes. Street lights are timed and the freeway has traffic. It's likely you won't get there much faster even if you do speed.</p>
    <p class="tip"><b>Don't drink and drive.</b> Many cab companies offer a free service to get you home safe.</p>
    <p class="tip"><b>Use your turn signals.</b> This gives an early warning to vehicles you may not be able to see.</p>
  </div>
  <div class="inner">
    <div class="inner__photo" role="img" aria-label="Photo of two people handing over car keys at a dealership"></div>
    <div class="inner__bar"><span>Have the Right Coverage</span><span>Model Safe Behavior</span></div>
    <div class="inner__body">
      <div class="col-coverage">
        <p>Many people don't know about the different kinds of insurance available. In addition to health insurance, we suggest:</p>
        <p><b>Auto Liability</b> (required by the state of Arizona in the amounts of $25,000 per person / $50,000 per accident, but a higher amount may be best ).</p>
        <p><b>Uninsured or Underinsured Motorist Coverage.</b> This protects YOU when the other driver doesn't have insurance or not enough.</p>
        <p><b>Medical Payments Coverage.</b> Up to $5,000 in coverage will be paid out to you no matter who is at fault in an accident and does not need to be reimbursed.</p>
        <p><b>Homeowners / Renters Insurance.</b> Protects you in case of injuries on your property as well as damage to your home from covered events.</p>
      </div>
      <div class="strip">
        <svg width="16" height="14" viewBox="0 0 16 14" aria-hidden="true"><path d="M2 1h12a1 1 0 0 1 1 1v7a1 1 0 0 1-1 1H7l-4 3v-3H2a1 1 0 0 1-1-1V2a1 1 0 0 1 1-1z" fill="#fff"/><circle cx="5" cy="5.5" r="1" fill="#15244a"/><circle cx="8" cy="5.5" r="1" fill="#15244a"/><circle cx="11" cy="5.5" r="1" fill="#15244a"/></svg>
        <div class="strip__contact">
          <svg width="13" height="13" viewBox="0 0 14 14" aria-hidden="true"><path d="M3 1l2 3-1.3 1.3a8 8 0 0 0 5 5L10 9l3 2-1 2c-6 0-11-5-11-11z" fill="none" stroke="#fff" stroke-width="1.3"/></svg>
          <svg width="13" height="13" viewBox="0 0 14 14" aria-hidden="true"><rect x="1" y="3" width="12" height="8" fill="none" stroke="#fff" stroke-width="1.3"/><path d="M1 3l6 5 6-5" fill="none" stroke="#fff" stroke-width="1.3"/></svg>
          <svg width="13" height="13" viewBox="0 0 14 14" aria-hidden="true"><circle cx="7" cy="7" r="6" fill="none" stroke="#fff" stroke-width="1.2"/><ellipse cx="7" cy="7" rx="2.6" ry="6" fill="none" stroke="#fff" stroke-width="1.1"/><path d="M1 7h12" stroke="#fff" stroke-width="1.1"/></svg>
          <svg width="13" height="15" viewBox="0 0 14 16" aria-hidden="true"><path d="M7 1a5 5 0 0 1 5 5c0 4-5 9-5 9S2 10 2 6a5 5 0 0 1 5-5z" fill="none" stroke="#fff" stroke-width="1.3"/><circle cx="7" cy="6" r="1.8" fill="#fff"/></svg>
        </div>
      </div>
      <div class="col-behavior">
        <p><b>Always buckle up.</b> Always put your children in car seats/boosters that are rated for their height and weight.</p>
        <h3>Never Text While Driving</h3>
        <p>Studies have shown that texting while driving is as dangerous as driving intoxicated.</p>
        <p><b>Show your children that no text is more important than your safety. It can wait.</b></p>
        <div class="contact">
          <h3>Contact Us</h3>
          <p>602.555.0148</p>
          <p>info@MarbrenLegal.com</p>
          <p>MarbrenLegal.com</p>
          <p>Marbren Legal Group 4870 N. 19th Avenue Suite B310 Phoenix AZ 85015</p>
        </div>
      </div>
    </div>
  </div>
</section>

</body>
</html>
```